Modern Quillby Tree Care Website

I need a website for a full service Tree Care company. The company provides tree pruning, tree removal, tree preservation, emergency services, stump grinding, and emergency tree services.

Target Market(s)

Customers that need tree services

Industry/Entity Type

Landscaping, Tree Services

Coding

Coded - Design and coding required

Number of Pages Required

5+ page

Font styles to use
Sans Serif

Requirements
Must have
• Good clean design that showcases the services the company provides.
Nice to have
• Services page; contact form, blog, home page, about page

```html
<!DOCTYPE html>
<html lang="en">
<head>
<meta charset="utf-8">
<title>Quillby Tree Care</title>
<link href="https://fonts.googleapis.com/css2?family=Bebas+Neue&family=Roboto:wght@400;500;700&display=swap" rel="stylesheet">
<style>
:root{
  --green:#7cc142;
  --green-dark:#6aaf33;
  --orange:#f7ae3b;
  --tan:#c8956a;
  --ink:#333;
  --body:#555;
  --field:#f0eeee;
  --night:#1d2a24;
  --white:#fff;
}
*{box-sizing:border-box;margin:0;padding:0}
html,body{width:1200px;height:4526px;overflow:hidden}
body{position:relative;font-family:'Roboto',Arial,sans-serif;color:var(--body);background:var(--white)}
.abs{position:absolute}
.display{font-family:'Bebas Neue',Impact,sans-serif;font-weight:400;letter-spacing:1px}
.photo{position:absolute}

/* Hero */
.hero{left:0;top:0;width:1200px;height:690px;background:linear-gradient(180deg,#6f7d86 0%,#8b9580 40%,#4e5b35 75%,#eef0ea 100%)}
.hero-shade{left:0;top:0;width:1200px;height:522px;background:rgba(30,35,30,.25)}
.logo{left:110px;top:24px;display:flex;align-items:center;gap:12px}
.logo-mark{width:40px;height:40px;background:var(--green)}
.logo-name{font-family:'Bebas Neue',sans-serif;font-size:44px;color:var(--white);letter-spacing:2px;line-height:1}
.nav{left:562px;top:0;display:flex;align-items:flex-start;height:105px}
.nav a{color:var(--white);text-decoration:none;font-size:14px;padding:66px 16px 0;height:105px;display:block}
.nav a.active{background:var(--green)}
.call{right:112px;top:20px;font-size:13px;color:var(--white)}
.call span{color:var(--green)}
.btn-est{left:966px;top:56px;width:122px;height:35px;background:var(--green);color:var(--white);font-size:14px;font-weight:700;display:flex;align-items:center;justify-content:center}
.hero-title{left:0;width:1200px;text-align:center;font-size:72px;line-height:1}
.hero-sub{left:0;top:350px;width:1200px;text-align:center;font-size:26px;color:var(--green);letter-spacing:2px}
.hero-btn{left:541px;top:390px;width:118px;height:31px;background:var(--green);color:var(--white);font-size:14px;font-weight:700;display:flex;align-items:center;justify-content:center}
.dots{left:1080px;top:292px;display:flex;flex-direction:column;gap:6px}
.dots i{display:block;width:14px;height:14px;border-radius:50%;border:2px solid var(--orange)}
.dots i.on{background:var(--green);border-color:var(--green)}

/* Welcome */
.faded-bg{left:0;top:690px;width:1200px;height:640px;background:linear-gradient(180deg,#f1f3ee,#e4eadb 60%,#ffffff)}
.welcome{left:110px;top:522px;width:1090px;height:515px;background:var(--white);border-bottom:5px solid #fbe7c4}
.welcome-kicker{left:18px;top:52px;font-size:21px;color:var(--ink)}
.welcome-title{left:18px;top:80px;font-size:50px;color:var(--green)}
.welcome-text{left:18px;top:150px;width:490px;font-size:14px;line-height:26px;color:var(--body)}
.welcome-text p+p{margin-top:26px}
.btn-outline{border:2px solid var(--orange);color:var(--orange);font-size:14px;display:flex;align-items:center;justify-content:center}
.welcome-btn{left:18px;top:399px;width:120px;height:34px}
.welcome-photo{left:572px;top:56px;width:406px;height:406px;background:linear-gradient(135deg,#7ea34a,#3f6d2a 60%,#2c4e1e)}

/* Services */
.kicker{left:0;width:1200px;text-align:center;font-size:20px;color:var(--ink)}
.section-title{left:0;width:1200px;text-align:center;font-size:50px;color:var(--green)}
.svc-row{left:0;top:1200px;width:1200px;display:flex}
.svc{width:200px;display:flex;flex-direction:column;align-items:center}
.svc-icon{width:70px;height:70px;background:#d9d9d9;border-radius:8px}
.svc.active .svc-icon{background:var(--green)}
.svc-label{margin-top:22px;font-family:'Bebas Neue',sans-serif;font-size:21px;letter-spacing:1px;color:var(--ink)}
.svc.active .svc-label{color:var(--orange)}
.svc-underline{left:190px;top:1316px;width:190px;height:5px;background:var(--orange)}
.svc-caret{left:277px;top:1308px;width:0;height:0;border-left:8px solid transparent;border-right:8px solid transparent;border-bottom:8px solid var(--orange)}
.svc-band{left:0;top:1325px;width:1200px;height:458px;background:var(--green)}
.svc-photo{left:110px;top:47px;width:472px;height:366px;background:linear-gradient(160deg,#b7bec0,#8a8f7a 45%,#5c6b35 80%);border:3px solid #ffffff33}
.svc-title{left:613px;top:60px;font-size:48px;color:var(--white)}
.svc-text{left:613px;top:118px;width:450px;font-size:14px;line-height:26px;color:var(--white)}
.svc-text p+p{margin-top:18px}
.svc-btn{left:613px;top:365px;width:122px;height:34px;border:2px solid var(--white);color:var(--white);font-size:14px;font-weight:700;display:flex;align-items:center;justify-content:center}

/* Contact form */
.form-title{left:0;width:1200px;text-align:center;font-size:44px}
.field{height:41px;background:var(--field);font-size:13px;color:var(--ink);display:flex;align-items:center;justify-content:space-between;padding:0 28px}
.send{left:362px;top:2189px;width:476px;height:42px;background:var(--green);color:var(--white);font-weight:700;font-size:16px;display:flex;align-items:center;justify-content:center;gap:26px;box-shadow:0 3px 0 #5f9a2d}

/* Why pick */
.why{left:0;top:2305px;width:1200px;height:626px;background:var(--green)}
.why svg.bg{position:absolute;left:0;top:0}
.why-title{left:0;top:62px;width:1200px;text-align:center;font-size:50px;color:var(--white)}
.feat{width:260px;display:flex;flex-direction:column;align-items:center;color:var(--white);font-size:16px;font-weight:500}
.feat-icon{width:72px;height:72px;border-radius:50%;border:3px solid var(--white);display:flex;align-items:center;justify-content:center;margin-bottom:18px}

/* Blog */
.card{top:3096px;width:306px;height:392px;border:1px solid #e6e6e6;background:var(--white)}
.card-photo{left:0;top:0;width:304px;height:184px;background:linear-gradient(150deg,#88a654,#3f6a2a 55%,#23401a)}
.card-title{left:0;top:210px;width:304px;text-align:center;font-size:21px;line-height:24px;color:var(--ink)}
.card-text{left:14px;top:268px;width:276px;text-align:center;font-size:13px;line-height:20px;color:var(--body)}
.card-link{left:0;top:356px;width:304px;text-align:center;font-size:14px;color:var(--ink)}
.all-news{left:539px;top:3518px;width:122px;height:34px}

/* CTA + footer */
.footer-bg{left:0;top:3844px;width:1200px;height:682px;background:linear-gradient(180deg,#2d3b33,var(--night) 40%,#17211c)}
.cta{left:109px;top:3674px;width:980px;height:293px;overflow:hidden;background:var(--green)}
.cta svg.bg{position:absolute;left:0;top:0}
.cta-title{left:0;top:44px;width:980px;text-align:center;font-size:50px;line-height:48px;color:var(--white)}
.cta-phones{left:240px;top:172px;font-size:36px;line-height:56px;color:var(--white);letter-spacing:2px}
.cta-divider{left:539px;top:165px;width:2px;height:110px;background:#ffffffaa}
.cta-btn{left:569px;top:183px;width:311px;height:70px;background:var(--orange);color:var(--white);font-size:50px;display:flex;align-items:center;justify-content:center}
.foot-logo{left:110px;top:4030px;display:flex;align-items:center;gap:16px}
.foot-logo .logo-mark{width:64px;height:64px}
.foot-logo .logo-name{font-size:72px;color:#a9b0ab}
.badge{left:710px;top:4010px;width:68px;height:119px;background:#2e7d32;border:3px solid #e9d98c}
.social{left:890px;top:4060px;display:flex;gap:26px}
.social i{display:block;width:32px;height:32px;border-radius:50%;border:3px solid var(--white)}
.social i:first-child{border-color:var(--green)}
.fcol{top:4208px;height:246px;border-left:1px solid #ffffff33}
.fcol .mark{position:absolute;left:0;top:20px;width:5px;height:46px;background:var(--green)}
.fcol h4{position:absolute;left:28px;top:32px;font-size:16px;font-weight:700;color:var(--white)}
.fcol .txt{position:absolute;left:28px;top:80px;font-size:13px;line-height:26px;color:var(--white)}
.links div{display:flex;align-items:center;gap:6px;margin-bottom:8px}
.links i{display:block;width:11px;height:11px;border-radius:50%;border:1.5px solid var(--green)}
.sub-field{position:absolute;left:28px;top:168px;width:262px;height:48px;border:1px solid #ffffff88;display:flex;align-items:center;justify-content:space-between;padding-left:24px;font-size:12px;color:#ccc}
.sub-field span.go{width:66px;height:46px;background:var(--green);display:flex;align-items:center;justify-content:center}
.foot-line{left:110px;top:4463px;width:980px;height:1px;background:#ffffff33}
.copy{left:0;top:4484px;width:1200px;text-align:center;font-size:12px;color:#bbb}
</style>
</head>
<body>

<!-- Hero -->
<div class="abs hero photo" role="img" aria-label="Arborist in a bucket lift trimming a tall tree against a cloudy sky"></div>
<div class="abs hero-shade"></div>
<div class="abs logo"><span class="logo-mark"></span><span class="logo-name">Quillby Tree Care</span></div>
<nav class="abs nav">
  <a class="active" href="#">Home</a><a href="#">About</a><a href="#">Services ▾</a><a href="#">Blog</a><a href="#">Contact Us</a>
</nav>
<div class="abs call">Call Us: <span>+00 000 0000</span></div>
<div class="abs btn-est">Free Estimate</div>
<h1 class="abs hero-title display" style="top:200px;color:var(--green)">Call Quillby for all</h1>
<div class="abs hero-title display" style="top:272px;color:var(--orange)">Your tree care needs</div>
<div class="abs hero-sub">SERVING LAFAYETTE AND SURROUNDING AREAS</div>
<div class="abs hero-btn">Free Estimate</div>
<div class="abs dots"><i class="on"></i><i></i><i></i></div>

<!-- Welcome -->
<div class="abs faded-bg photo" role="img" aria-label="Faded forest backdrop"></div>
<section class="abs welcome">
  <div class="abs welcome-kicker">Welcome to</div>
  <h2 class="abs welcome-title display">Quillby Tree Care</h2>
  <div class="abs welcome-text">
    <p>At Quillby Tree Care, we are more than just a tree service company, we are stewards of our beautiful trees. With a passion deeply rooted in arboriculture, we embark on a mission to promote the health, beauty, and safety of your trees and landscapes.</p>
    <p>Whether it's expert tree trimming to enhance aesthetics, meticulous tree removal to mitigate hazards, or comprehensive tree health assessments to ensure safety, we approach each task with unwavering dedication and attention to detail.</p>
  </div>
  <div class="abs btn-outline welcome-btn">Read More</div>
  <div class="abs welcome-photo photo" role="img" aria-label="Collage of arborists trimming hedges, climbing and using a chainsaw"></div>
</section>

<!-- Services -->
<div class="abs kicker" style="top:1102px">Our Services</div>
<h2 class="abs section-title display" style="top:1130px">Quillby Tree Care Services</h2>
<div class="abs svc-row">
  <div class="svc"><div class="svc-icon" role="img" aria-label="Tree pruning illustration"></div><div class="svc-label">Tree Pruning</div></div>
  <div class="svc active"><div class="svc-icon" role="img" aria-label="Tree removal illustration"></div><div class="svc-label">Tree Removal</div></div>
  <div class="svc"><div class="svc-icon" role="img" aria-label="Tree preservation illustration"></div><div class="svc-label">Tree Preservation</div></div>
  <div class="svc"><div class="svc-icon" role="img" aria-label="Emergency services illustration"></div><div class="svc-label">Emergency Services</div></div>
  <div class="svc"><div class="svc-icon" role="img" aria-label="Stump grinding illustration"></div><div class="svc-label">Stump Grinding</div></div>
  <div class="svc"><div class="svc-icon" role="img" aria-label="Emergency tree services illustration"></div><div class="svc-label">Emergency Tree Services</div></div>
</div>
<div class="abs svc-caret"></div>
<div class="abs svc-underline"></div>
<section class="abs svc-band">
  <div class="abs svc-photo photo" role="img" aria-label="Worker beside a felled tree trunk and a wood chipper"></div>
  <h3 class="abs svc-title display">Tree Removal</h3>
  <div class="abs svc-text">
    <p>Lorem ipsum dolor sit amet, consectetur adipiscing elit, sed do eiusmod tempor incididunt ut labore et dolore magna aliqua. Ut enim ad minim veniam, quis nostrud exercitation ullamco laboris nisi ut aliquip ex ea commodo consequat.</p>
    <p>Duis aute irure dolor in reprehenderit in voluptate velit esse cillum dolore eu fugiat nulla pariatur. Excepteur sint occaecat cupidatat non proident, sunt in culpa qui officia deserunt mollit anim id est laborum.</p>
  </div>
  <div class="abs svc-btn">Read More</div>
</section>

<!-- Contact form -->
<div class="abs form-title display" style="top:1846px;color:var(--ink)">Interested in</div>
<h2 class="abs form-title display" style="top:1898px;color:var(--green)">Speaking with our team?</h2>
<div class="abs field" style="left:110px;top:1985px;width:479px">First Name</div>
<div class="abs field" style="left:611px;top:1985px;width:477px">Laste Name</div>
<div class="abs field" style="left:110px;top:2052px;width:479px">Email</div>
<div class="abs field" style="left:611px;top:2052px;width:477px">Phone Number</div>
<div class="abs field" style="left:110px;top:2119px;width:479px">Address
  <svg width="12" height="16" viewBox="0 0 12 16"><path d="M6 0a6 6 0 0 0-6 6c0 4.5 6 10 6 10s6-5.5 6-10a6 6 0 0 0-6-6z" fill="#222"/></svg></div>
<div class="abs field" style="left:611px;top:2119px;width:477px">Service Of Interest
  <svg width="10" height="6" viewBox="0 0 10 6"><path d="M0 0h10L5 6z" fill="#222"/></svg></div>
<div class="abs send">SEND
  <svg width="28" height="12" viewBox="0 0 28 12"><path d="M0 6h26M21 1l5 5-5 5" stroke="#fff" stroke-width="2" fill="none"/></svg></div>

<!-- Why pick -->
<section class="abs why">
  <svg class="bg" width="1200" height="626" viewBox="0 0 1200 626">
    <polygon points="0,0 220,0 0,440" fill="var(--tan)"/>
    <polygon points="975,0 1200,0 1200,440" fill="var(--orange)"/>
  </svg>
  <h2 class="abs why-title display">Why pick Quillby Tree Care?</h2>
  <div class="abs feat" style="left:67px;top:152px"><div class="feat-icon"><svg width="36" height="36" viewBox="0 0 36 36"><circle cx="18" cy="15" r="10" fill="none" stroke="#fff" stroke-width="3"/><path d="M12 24l-3 10 9-4 9 4-3-10" fill="none" stroke="#fff" stroke-width="3"/></svg></div>Licensed and Insured</div>
  <div class="abs feat" style="left:341px;top:152px"><div class="feat-icon"><svg width="40" height="40" viewBox="0 0 40 40"><circle cx="20" cy="20" r="15" fill="none" stroke="#fff" stroke-width="3"/><text x="20" y="26" text-anchor="middle" font-family="Roboto,sans-serif" font-size="15" font-weight="700" fill="#fff">24</text></svg></div>24-Hours Emergency Services</div>
  <div class="abs feat" style="left:615px;top:152px"><div class="feat-icon"><svg width="30" height="38" viewBox="0 0 30 38"><path d="M15 2a12 12 0 0 0-12 12c0 9 12 22 12 22s12-13 12-22A12 12 0 0 0 15 2z" fill="none" stroke="#fff" stroke-width="3"/><circle cx="15" cy="14" r="4" fill="#fff"/></svg></div>Locally Owned &amp; Operated</div>
  <div class="abs feat" style="left:889px;top:152px"><div class="feat-icon"><svg width="40" height="28" viewBox="0 0 40 28"><path d="M6 22a14 14 0 0 1 28 0z" fill="#fff"/><rect x="2" y="22" width="36" height="4" fill="#fff"/></svg></div>Professional Work</div>
  <div class="abs feat" style="left:195px;top:359px"><div class="feat-icon"><svg width="32" height="38" viewBox="0 0 32 38"><path d="M16 2l13 5v10c0 9-6 16-13 19C9 33 3 26 3 17V7z" fill="none" stroke="#fff" stroke-width="3"/><path d="M10 18l5 5 8-9" fill="none" stroke="#fff" stroke-width="3"/></svg></div>Safety is Our No.1 Priority</div>
  <div class="abs feat" style="left:469px;top:359px"><div class="feat-icon"><svg width="30" height="36" viewBox="0 0 30 36"><rect x="3" y="2" width="24" height="32" rx="2" fill="none" stroke="#fff" stroke-width="3"/><path d="M8 11h14M8 18h14M8 25h9" stroke="#fff" stroke-width="3"/></svg></div>Free Estimates</div>
  <div class="abs feat" style="left:743px;top:359px"><div class="feat-icon"><svg width="26" height="38" viewBox="0 0 26 38"><rect x="2" y="2" width="22" height="34" fill="none" stroke="#fff" stroke-width="3"/><rect x="7" y="9" width="12" height="14" fill="#fff"/></svg></div>Licensed Arborist on Staff</div>
</section>

<!-- Blog -->
<div class="abs kicker" style="top:2998px">Our Blog's</div>
<h2 class="abs section-title display" style="top:3028px">Latest News &amp; Updates</h2>
<article class="abs card" style="left:110px">
  <div class="abs card-photo photo" role="img" aria-label="Gardener trimming a hedge with shears"></div>
  <h3 class="abs card-title display">Lorem ipsum is placeholder text<br>commonly used the graphic.</h3>
  <p class="abs card-text">Lorem ipsum dolor sit amet, consectetur adipiscing elit, sed do eiusmod tempor incididunt ut labore et dolore magna aliqua. Ut enim ad minim veniam...</p>
  <div class="abs card-link">Read More</div>
</article>
<article class="abs card" style="left:446px">
  <div class="abs card-photo photo" role="img" aria-label="Hedge shears cutting green leaves"></div>
  <h3 class="abs card-title display">Lorem ipsum is placeholder text<br>commonly used the graphic.</h3>
  <p class="abs card-text">Lorem ipsum dolor sit amet, consectetur adipiscing elit, sed do eiusmod tempor incididunt ut labore et dolore magna aliqua. Ut enim ad minim veniam...</p>
  <div class="abs card-link">Read More</div>
</article>
<article class="abs card" style="left:782px">
  <div class="abs card-photo photo" role="img" aria-label="Arborist climbing a tree with a chainsaw"></div>
  <h3 class="abs card-title display">Lorem ipsum is placeholder text<br>commonly used the graphic.</h3>
  <p class="abs card-text">Lorem ipsum dolor sit amet, consectetur adipiscing elit, sed do eiusmod tempor incididunt ut labore et dolore magna aliqua. Ut enim ad minim veniam...</p>
  <div class="abs card-link">Read More</div>
</article>
<div class="abs btn-outline all-news">All New's</div>

<!-- CTA and footer -->
<div class="abs footer-bg photo" role="img" aria-label="Dark forest canopy backdrop"></div>
<section class="abs cta">
  <svg class="bg" width="980" height="293" viewBox="0 0 980 293">
    <polygon points="0,0 120,0 0,240" fill="var(--tan)"/>
    <polygon points="860,0 980,0 980,240" fill="var(--orange)"/>
  </svg>
  <h2 class="abs cta-title display">Call us today to see how we can help<br>you with all of your tree needs:</h2>
  <svg class="abs" style="left:102px;top:172px" width="110" height="90" viewBox="0 0 110 90">
    <path d="M8 30c0-14 22-22 47-22s47 8 47 22l-16 6-6-12c-16-4-34-4-50 0l-6 12z" fill="#fff"/>
    <path d="M32 40h46l18 40H14z" fill="#fff"/>
    <circle cx="55" cy="60" r="13" fill="var(--green)"/>
    <circle cx="55" cy="60" r="6" fill="#fff"/>
  </svg>
  <div class="abs cta-phones">(337) 555-0142<br>(318) 555-0187</div>
  <div class="abs cta-divider"></div>
  <div class="abs cta-btn display">Free Estimate</div>
</section>

<footer>
  <div class="abs foot-logo"><span class="logo-mark"></span><span class="logo-name">Quillby Tree Care</span></div>
  <div class="abs badge" role="img" aria-label="Certification badge"></div>
  <div class="abs social"><i></i><i></i><i></i><i></i></div>

  <div class="abs fcol" style="left:110px;width:385px">
    <span class="mark"></span><h4>To Reach Us</h4>
    <div class="txt">
      <div><svg width="9" height="12" viewBox="0 0 12 16"><path d="M6 0a6 6 0 0 0-6 6c0 4.5 6 10 6 10s6-5.5 6-10a6 6 0 0 0-6-6z" fill="#7cc142"/></svg> 4810 Oakridge Rd.<br>Suite 210, Lafayette, LA 70503</div>
      <div style="margin-top:28px"><svg width="11" height="11" viewBox="0 0 16 16"><path d="M3 1l3 3-2 3c1 2 3 4 5 5l3-2 3 3-2 2C7 15 1 9 1 3z" fill="#7cc142"/></svg> (337) 555-0142 (318) 555-0187</div>
      <div style="margin-top:28px"><svg width="12" height="10" viewBox="0 0 16 12"><rect x="1" y="1" width="14" height="10" fill="none" stroke="#7cc142" stroke-width="2"/><path d="M1 1l7 6 7-6" fill="none" stroke="#7cc142" stroke-width="2"/></svg> hello@quillbytreecare.com</div>
    </div>
  </div>
  <div class="abs fcol" style="left:495px;width:305px">
    <span class="mark"></span><h4>Quick Links</h4>
    <div class="txt links">
      <div><i></i>Home</div><div><i></i>About Us</div><div><i></i>Services</div><div><i></i>Blog</div><div><i></i>Contact Us</div>
    </div>
  </div>
  <div class="abs fcol" style="left:800px;width:290px">
    <span class="mark"></span><h4>Subscribe</h4>
    <div class="txt" style="width:240px;font-size:12px">Neque porro quisquam est qui dolorem ipsum quia dolor sit amet,</div>
    <div class="sub-field">Email Address<span class="go"><svg width="18" height="18" viewBox="0 0 18 18"><path d="M1 8l16-7-5 16-3-6z" fill="#fff"/></svg></span></div>
  </div>
  <div class="abs foot-line"></div>
  <div class="abs copy">Quillby Tree Care© 2024 All Rights Reserved.</div>
</footer>

</body>
</html>
```